4 page website for our new business,
www.Velna Crest Bathrooms.example
We will provide the follwing service
1st Home page, bathroom renvovations, make over redesign etc
2nd page Tiling service
3rd page Waterproofing
4th page Galllery
The home will maily focus on the core business bathroom renovation, customer should able request quote, via entering thier info eg. name and contact number and select the 3 services
Need area for testimonials that will scroll
Maybe a banner which may flash varies pic of different design
Maybe a area for giving reasons why customer should go with us for they job
simple site which will grentrate leads, create presece, build brand.
We've just had the logo design, which allow you to create theme.
Target Market(s)
home owner's mum and dad
Look and feel
Each slider illustrates characteristics of the customer's brand and the style your logo design should communicate.

```html
<!DOCTYPE html>
<html lang="en">
<head>
<meta charset="utf-8">
<title>Velna Crest Bathrooms</title>
<link href="https://fonts.googleapis.com/css2?family=PT+Sans:wght@400;700&family=Yanone+Kaffeesatz:wght@400;500&display=swap" rel="stylesheet">
<style>
:root{
  --ink:#1d2a4a;
  --text:#4a4a4a;
  --navy:#1b2e63;
  --sky:#86d3f3;
  --sky-line:#a9e0f7;
  --band:#e6e7e9;
  --pale:#eef0f4;
  --black:#000;
  --topbar:#4a4a4a;
  --nav-top:#a9abae;
  --nav-bot:#6f7174;
  --btn-top:#4c9ec4;
  --btn-bot:#2f7ea6;
  --brand:#2a8fd0;
  --quote-head:#5d5f62;
  --field:#ffffff;
  --line:#c9cbce;
}
*{box-sizing:border-box;margin:0;padding:0}
html,body{width:1200px;height:999px;overflow:hidden}
body{position:relative;background:#fff;font-family:"PT Sans",sans-serif;color:var(--text)}
.abs{position:absolute}
.topbar{left:0;top:0;width:1200px;height:24px;background:var(--black);border-top:10px solid var(--topbar)}
.band{left:0;top:372px;width:1200px;height:269px;background:var(--band)}
.lower{left:0;top:641px;width:1200px;height:250px;background:var(--pale)}
.footer{left:0;top:891px;width:1200px;height:108px;background:var(--black)}

.brand{left:163px;top:42px;display:flex;align-items:center;gap:10px}
.brand-dot{width:78px;height:78px;border-radius:50%;background:var(--brand)}
.brand-name{font-size:15px;font-weight:700;color:var(--brand);width:110px;line-height:18px}

.search{left:766px;top:41px;width:168px;height:29px;border:1px solid #d6d6d6;border-radius:4px;background:#fff;font-size:11px;color:#333;padding:7px 9px}
.search svg{position:absolute;right:7px;top:6px}
.social{width:22px;height:22px;border-radius:3px}
.s1{background:#3fb1e6}.s2{background:#3b5a9a}

.nav{left:520px;top:89px;width:515px;height:31px;border-radius:4px;background:linear-gradient(var(--nav-top),var(--nav-bot));display:flex;box-shadow:0 8px 8px -6px rgba(0,0,0,.35)}
.nav a{color:#fff;text-decoration:none;font-size:12px;text-align:center;line-height:31px;border-right:1px solid #55575a;text-shadow:0 1px 1px rgba(0,0,0,.4)}
.nav a:last-child{border-right:0}

.hero{left:163px;top:140px;width:601px;height:278px;border:1px solid #cfcfcf;background:linear-gradient(120deg,#b9a68e 0%,#d9c7a6 35%,#a8456a 50%,#e8dfcf 75%,#c9b9a3 100%);box-shadow:0 12px 12px -8px rgba(0,0,0,.35)}

.quote{left:774px;top:140px;width:261px;height:278px;border:1px solid #d3d3d3;background:linear-gradient(#fff 55%,#f0f0f0);padding:6px 5px}
.quote-head{background:var(--quote-head);color:#fff;font-family:"Yanone Kaffeesatz",sans-serif;font-size:20px;height:26px;line-height:26px;padding-left:6px;border:1px solid #444}
.quote label{display:block;font-size:11px;color:#555;margin:12px 0 4px 0}
.field{height:29px;border:1px solid var(--line);background:var(--field);font-size:11px;color:#555;padding:7px 10px;position:relative}
.field svg{position:absolute;right:7px;top:7px}

.svc{top:447px;width:281px;height:162px;background:var(--sky);box-shadow:0 10px 10px -8px rgba(0,0,0,.35)}
.svc h2{font-weight:400;font-size:17px;color:var(--ink);height:37px;line-height:44px;padding-left:15px;border-bottom:1px solid var(--sky-line)}
.svc .pic{position:absolute;left:16px;top:56px;width:108px;height:83px;box-shadow:1px 2px 3px rgba(0,0,0,.4)}
.svc p{position:absolute;left:136px;top:55px;width:132px;font-size:12px;line-height:16.5px;color:var(--ink);text-align:justify}
.more{position:absolute;right:11px;top:150px;width:56px;height:21px;border-radius:6px;background:linear-gradient(var(--btn-top),var(--btn-bot));color:#fff;font-size:12px;text-align:center;line-height:21px}

.sec-title{font-size:16px;color:var(--navy);font-weight:400}
.rule{height:1px;background:#9a9da3}
.testi-pic{left:164px;width:138px;height:72px;border:1px solid #ccc;background:linear-gradient(90deg,#2d2f35,#56505a 50%,#2a2c33)}
.testi-text{left:318px;width:396px;font-size:12px;line-height:18.3px;color:#444;text-align:justify}
.thumb{width:89px;height:64px;border:1px solid #c9c9c9;background:linear-gradient(135deg,#e9ebee,#b9bdc3)}

.foot-links{left:163px;top:922px;font-size:11px;color:#fff}
.foot-links span{margin:0 7px}
.copy{left:163px;top:945px;font-size:10.5px;color:#fff}
</style>
</head>
<body>
<div class="abs topbar"></div>
<div class="abs band"></div>
<div class="abs lower"></div>
<div class="abs footer"></div>

<div class="abs brand"><div class="brand-dot"></div><div class="brand-name">Velna Crest Bathrooms</div></div>

<div class="abs search">Search
  <svg width="16" height="16" viewBox="0 0 16 16"><circle cx="6.5" cy="6.5" r="4.5" fill="none" stroke="#aaa" stroke-width="2"/><line x1="10" y1="10" x2="14.5" y2="14.5" stroke="#aaa" stroke-width="2.5"/></svg>
</div>
<div class="abs social s1" style="left:981px;top:44px"></div>
<div class="abs social s2" style="left:1012px;top:44px"></div>

<nav class="abs nav">
  <a href="#" style="width:108px">HOME</a>
  <a href="#" style="width:101px">ABOUT US</a>
  <a href="#" style="width:100px">SERVICES</a>
  <a href="#" style="width:100px">QUICK QUOTE</a>
  <a href="#" style="width:106px">CONTACT US</a>
</nav>

<div class="abs hero" role="img" aria-label="Banner photo: consultant at a desk handing over a folder to a customer"></div>

<form class="abs quote">
  <div class="quote-head">QUICK QUOTE</div>
  <label>Name</label><div class="field"></div>
  <label>Number</label><div class="field"></div>
  <label>Service Needed</label>
  <div class="field">Tiling Service
    <svg width="9" height="14" viewBox="0 0 9 14"><path d="M4.5 1 8 5.5H1z M4.5 13 8 8.5H1z" fill="#444"/></svg>
  </div>
</form>

<section class="abs svc" style="left:163px">
  <h2>Bathroom Renvovations</h2>
  <div class="pic" role="img" aria-label="Photo of a renovated bright bathroom" style="background:linear-gradient(135deg,#e8e2d2,#a89a80)"></div>
  <p>Lorem Ipsum is simply dummy text of the printing and typesetting industry. Lorem Ipsum has</p>
  <div class="more">More</div>
</section>
<section class="abs svc" style="left:459px">
  <h2>Tiling Services</h2>
  <div class="pic" role="img" aria-label="Photo of hands laying terracotta floor tiles" style="background:linear-gradient(135deg,#8a7a6a,#c8784a 60%,#b06a40)"></div>
  <p>Lorem Ipsum is simply dummy text of the printing and typesetting industry. Lorem Ipsum has</p>
  <div class="more">More</div>
</section>
<section class="abs svc" style="left:755px">
  <h2>Waterproffing</h2>
  <div class="pic" role="img" aria-label="Photo of a worker applying waterproofing to a wall" style="background:linear-gradient(135deg,#7a8aa8,#c9c6c0)"></div>
  <p>Lorem Ipsum is simply dummy text of the printing and typesetting industry. Lorem Ipsum has</p>
  <div class="more">More</div>
</section>

<h3 class="abs sec-title" style="left:163px;top:660px">Testimonials</h3>
<div class="abs rule" style="left:165px;top:689px;width:547px"></div>
<div class="abs testi-pic" style="top:702px" role="img" aria-label="Photo of a group of business people"></div>
<p class="abs testi-text" style="top:703px">Lorem Ipsum is simply dummy text of the printing and typesetting industry. Lorem Ipsum has been the industry's standard dummy text ever since the 1500s when an unknown printer took a galley of type and scrambled it to make</p>
<div class="abs testi-pic" style="top:795px" role="img" aria-label="Photo of a group of business people"></div>
<p class="abs testi-text" style="top:796px">Lorem Ipsum is simply dummy text of the printing and typesetting industry. Lorem Ipsum has been the industry's standard dummy text ever since the 1500s when an unknown printer took a galley of type and scrambled it to make</p>

<h3 class="abs sec-title" style="left:755px;top:660px">Photo Gallery</h3>
<div class="abs rule" style="left:757px;top:689px;width:279px"></div>
<div class="abs thumb" style="left:757px;top:702px" role="img" aria-label="Gallery photo of a white bathroom"></div>
<div class="abs thumb" style="left:853px;top:702px" role="img" aria-label="Gallery photo of a white bathroom"></div>
<div class="abs thumb" style="left:948px;top:702px;background:linear-gradient(135deg,#c9cdd4,#8a7a66)" role="img" aria-label="Gallery photo of a bathroom with freestanding tub"></div>
<div class="abs thumb" style="left:756px;top:772px" role="img" aria-label="Gallery photo of a bathroom vanity"></div>
<div class="abs thumb" style="left:853px;top:772px;background:linear-gradient(135deg,#d8d6d2,#5a4a40)" role="img" aria-label="Gallery photo of a bathroom with dark cabinetry"></div>
<div class="abs thumb" style="left:948px;top:772px;background:linear-gradient(135deg,#eef2f6,#a9c6d6)" role="img" aria-label="Gallery photo of a bright blue-lit bathroom"></div>

<div class="abs foot-links">Home<span>|</span>About Us<span>|</span>Services<span>|</span>Quick Quote<span>|</span>Contact Us</div>
<div class="abs copy">Copyrights @ 2012 All Rights Reserved</div>
<div class="abs social s1" style="left:976px;top:931px"></div>
<div class="abs social s2" style="left:1007px;top:931px"></div>
</body>
</html>
```